Real Estate "For Sale" Sign for construction company

We need a sign that we can use to hang on a post and place on the road when we sell a property. The sign will be simple and will need to mainly feature our logo (files attached), as well as the words "For Sale", and then our phone number "(555) 617 3489". The sign will hang on a post that'll look something like the attached picture.

Target Market(s)

Home buyers

Industry/Entity Type

Real Estate

Font styles to use
Serif
Sans Serif

Colors
0054AA
0677BA
7BADD7
CADEEF
E8F1F8
0094D4
00A9DD
6FCCEA
C7EBF8
E9F6FB

Requirements
Must have
• For Sale & our phone number

```html
<!DOCTYPE html>
<html lang="en">
<head>
<meta charset="utf-8">
<title>Bluecrest Ridge Properties – For Sale Sign</title>
<link rel="stylesheet" href="https://fonts.googleapis.com/css2?family=Anton&family=Big+Shoulders+Display:wght@800&family=Montserrat:wght@500&display=swap">
<style>
  :root {
    --white: #ffffff;
    --sky: #8fd8f6;
    --royal: #0a52a5;
    --brand: #1a7cc4;
    --navy: #121f4b;
  }
  html, body {
    margin: 0;
    padding: 0;
    overflow: hidden;
    background: var(--white);
  }
  .sign {
    position: relative;
    width: 974px;
    height: 1200px;
    overflow: hidden;
    background: var(--white);
  }
  .sign__sky-band {
    position: absolute;
    left: 0;
    top: 400px;
    width: 974px;
    height: 520px;
    background: var(--sky);
  }
  .sign__ground-band {
    position: absolute;
    left: 0;
    top: 915px;
    width: 974px;
    height: 285px;
    background: var(--navy);
    border-top: 5px solid var(--white);
  }
  .brand {
    position: absolute;
    top: 36px;
    left: 0;
    width: 100%;
    text-align: center;
    color: var(--brand);
    font-family: "Montserrat", sans-serif;
    font-weight: 500;
  }
  .brand__mark {
    width: 140px;
    height: 140px;
    margin: 0 auto 18px;
    border-radius: 50%;
    background: var(--brand);
  }
  .brand__name {
    margin: 0;
    font-size: 60px;
    line-height: 1;
    letter-spacing: 0.5px;
  }
  .brand__tagline {
    margin: 18px 0 0;
    font-size: 20px;
    letter-spacing: 21px;
    padding-left: 21px;
  }
  .headline, .phone-number {
    position: absolute;
    left: 0;
    width: 974px;
    overflow: visible;
  }
  .headline { top: 520px; height: 270px; }
  .headline__text {
    font-family: "Anton", sans-serif;
    font-size: 257px;
    fill: var(--royal);
    stroke: var(--white);
    stroke-width: 4px;
    paint-order: stroke;
    filter: drop-shadow(10px 12px 0 var(--white));
  }
  .call-badge {
    position: absolute;
    left: 420px;
    top: 818px;
    width: 134px;
    height: 134px;
    border-radius: 50%;
    background: var(--white);
  }
  .call-badge svg { width: 134px; height: 134px; display: block; }
  .phone-number { top: 960px; height: 190px; }
  .phone-number__text {
    font-family: "Big Shoulders Display", sans-serif;
    font-weight: 800;
    font-size: 200px;
    fill: var(--white);
  }
</style>
</head>
<body>
<main class="sign">
  <div class="sign__sky-band" role="img" aria-label="Light blue mountain range band"></div>
  <div class="sign__ground-band" role="img" aria-label="Dark navy foreground ridge band"></div>

  <header class="brand">
    <div class="brand__mark"></div>
    <p class="brand__name">Bluecrest Ridge</p>
    <p class="brand__tagline">PROPERTIES</p>
  </header>

  <svg class="headline" viewBox="0 0 974 270">
    <text class="headline__text" x="77" y="243" textLength="832" lengthAdjust="spacingAndGlyphs">FOR SALE</text>
  </svg>

  <div class="call-badge">
    <svg viewBox="0 0 134 134" aria-hidden="true">
      <path fill="var(--royal)" d="M40 42 c6-6 12-6 15 0 l7 12 c2 5 0 8-4 11 c-3 2-3 5-1 8 c5 8 11 14 19 19 c3 2 6 2 8-1 c3-4 6-6 11-4 l12 7 c6 3 6 9 0 15 c-6 6-16 7-26 2 c-18-9-33-24-42-42 c-5-10-4-21 1-27 z"/>
      <g fill="none" stroke="var(--royal)" stroke-width="6" stroke-linecap="round">
        <path d="M72 52 a12 12 0 0 1 12 12"/>
        <path d="M72 38 a26 26 0 0 1 26 26"/>
        <path d="M72 24 a40 40 0 0 1 40 40"/>
      </g>
    </svg>
  </div>

  <svg class="phone-number" viewBox="0 0 974 190">
    <text class="phone-number__text" x="110" y="168" textLength="757" lengthAdjust="spacingAndGlyphs">(555) 617 3489</text>
  </svg>
</main>
</body>
</html>
```